For Lease sign for Property management company in Kansas City

We need someone to take our information and design a standard for lease sign that we can put in front of each of our buildings. I would love for it to do its job of letting people know there are units available but also be unique somehow. Also the aspect ratio of the design would ideally be 4 wide by 3 tall but we open to other ideas. It will be a larger yard sign.

Target Market(s)

Potential Tenants

Industry/Entity Type

Real Estate Development

Font styles to use
Sans Serif

Requirements
Must have
• Our logo, our website (www.quillstead-properties.com), our phone number (816) 555-2719.
Nice to have
• Some how say "For Lease"
Sign to be 4' wide by 3' tall
If there was a place to put the building name that would be cool but not ne
Should not have
• Nothing that I can think of

```html
<!DOCTYPE html>
<html lang="en">
<head>
<meta charset="utf-8">
<title>For Lease Yard Sign – Quillstead Properties</title>
<link href="https://fonts.googleapis.com/css2?family=Bebas+Neue&family=Montserrat:wght@500;700;800&display=swap" rel="stylesheet">
<style>
  :root {
    --backdrop: #828080;
    --sign-red: #be1e2d;
    --headline-shadow: #8e1320;
    --sign-gold: #fbb03b;
    --sign-white: #ffffff;
    --ink-grey: #58595b;
  }
  html, body {
    margin: 0;
    padding: 0;
    width: 959px;
    height: 1200px;
    overflow: hidden;
    background: var(--backdrop);
  }
  .canvas {
    position: relative;
    width: 959px;
    height: 1200px;
  }
  .lease-sign {
    position: absolute;
    left: 40px;
    top: 270px;
    width: 880px;
    height: 660px;
    background: var(--sign-white);
    overflow: hidden;
  }
  .lease-sign__band {
    position: absolute;
    inset: 0;
    width: 880px;
    height: 660px;
  }
  .lease-sign__headline {
    position: absolute;
    left: 0;
    right: 0;
    top: 18px;
    margin: 0;
    text-align: center;
    font-family: "Bebas Neue", "Oswald", sans-serif;
    font-weight: 400;
    font-size: 254px;
    line-height: 1;
    letter-spacing: 1px;
    color: var(--sign-gold);
    text-shadow: 7px 5px 0 var(--headline-shadow);
  }
  .lease-sign__phone {
    position: absolute;
    left: 0;
    right: 0;
    top: 258px;
    margin: 0;
    text-align: center;
    font-family: "Montserrat", sans-serif;
    font-weight: 500;
    font-size: 57px;
    line-height: 1;
    color: var(--sign-white);
  }
  .lease-sign__web {
    position: absolute;
    left: 0;
    right: 0;
    top: 332px;
    margin: 0;
    text-align: center;
    font-family: "Montserrat", sans-serif;
    font-weight: 800;
    font-size: 25px;
    line-height: 1;
    color: var(--sign-white);
  }
  .brand {
    position: absolute;
    left: 125px;
    top: 448px;
    display: flex;
    align-items: center;
    gap: 30px;
  }
  .brand__dot {
    width: 168px;
    height: 168px;
    border-radius: 50%;
    background: var(--sign-gold);
    flex: none;
  }
  .brand__name {
    font-family: "Montserrat", sans-serif;
    font-weight: 800;
    font-size: 50px;
    line-height: 1.05;
    color: var(--sign-red);
    letter-spacing: 1px;
  }
</style>
</head>
<body>
<main class="canvas">
  <section class="lease-sign" aria-label="For lease yard sign">
    <svg class="lease-sign__band" viewBox="0 0 880 660" aria-hidden="true">
      <path d="M0 0 H880 V330 Q440 460 0 366 Z" fill="var(--sign-gold)" transform="translate(0 10)"/>
      <path d="M0 0 H880 V330 Q440 460 0 366 Z" fill="var(--sign-red)"/>
    </svg>
    <h1 class="lease-sign__headline">For Lease</h1>
    <p class="lease-sign__phone">Call: (816) 555-2719</p>
    <p class="lease-sign__web">www.quillstead-properties.com</p>
    <div class="brand">
      <span class="brand__dot" aria-hidden="true"></span>
      <span class="brand__name">QUILLSTEAD<br>PROPERTIES</span>
    </div>
  </section>
</main>
</body>
</html>
```